Zielgruppe
Endkunde ist eine Immobilienfirma ((Bauträger)
Aufgabenstellung
Das Design soll für eine Präsentationsmappe erstellt werden und die Bemaßung sowie Farbigleit der vorgegebnen pdf-Datei beinhalten. Es soll in den Hausfarben , nebst den Backround in grau, gehalten werden.

```html
<!DOCTYPE html>
<html lang="de">
<head>
<meta charset="utf-8">
<title>Präsentationsmappe – Wohnwert Elbland AG</title>
<link rel="stylesheet" href="https://fonts.googleapis.com/css2?family=Noticia+Text&family=Source+Sans+3:wght@400&display=swap">
<style>
  :root {
    --paper: #ffffff;
    --grey-light: #c6c7c6;
    --grey-dark: #5b5a5b;
    --brand-red: #8b2522;
    --text-grey: #5b5a5b;
    --white: #ffffff;
    --guide-cyan: #6fcbe6;
    --cut-pink: #e26aa0;
    --pocket-edge: #cfcfcf;
    --photo-light: #f2f5f5;
    --photo-mid: #9fbcbc;
    --photo-dark: #2f5558;
  }
  html, body {
    margin: 0;
    padding: 0;
    width: 1200px;
    height: 1200px;
    overflow: hidden;
    background: var(--paper);
  }
  .folder-layout { display: block; width: 1200px; height: 1200px; }
  .panel-light { fill: var(--grey-light); }
  .panel-dark { fill: var(--grey-dark); }
  .band-red { fill: var(--brand-red); }
  .pocket-flap { fill: var(--paper); stroke: var(--pocket-edge); stroke-width: 1.5; }
  .guide { stroke: var(--guide-cyan); stroke-width: 0.7; fill: none; }
  .cut-line { stroke: var(--cut-pink); stroke-width: 0.7; fill: none; stroke-dasharray: 3 2; }
  .slit { stroke: var(--cut-pink); stroke-width: 0.8; fill: none; }
  .brand-mark { fill: var(--brand-red); }
  .brand-name {
    font-family: "Noticia Text", Georgia, serif;
    fill: var(--brand-red);
    font-weight: 400;
  }
  .brand-url {
    font-family: "Noticia Text", Georgia, serif;
    fill: var(--text-grey);
  }
  .band-url {
    font-family: "Source Sans 3", Arial, sans-serif;
    fill: var(--white);
    font-size: 18px;
  }
  .slogan {
    font-family: "Noticia Text", Georgia, serif;
    fill: var(--white);
  }
  .contact {
    font-family: "Source Sans 3", Arial, sans-serif;
    font-size: 9.4px;
  }
  .contact-dark { fill: var(--text-grey); }
  .contact-light { fill: var(--white); }
</style>
</head>
<body>
<svg class="folder-layout" viewBox="0 0 1200 1200" xmlns="http://www.w3.org/2000/svg">
  <defs>
    <linearGradient id="towerPhoto" x1="0" y1="0" x2="1" y2="1">
      <stop offset="0" stop-color="var(--photo-light)"/>
      <stop offset="0.45" stop-color="var(--photo-mid)"/>
      <stop offset="1" stop-color="var(--photo-dark)"/>
    </linearGradient>
    <clipPath id="flapClip">
      <path d="M151 158 L60 178 Q29 188 29 206 L29 806 Q29 820 45 826 L151 847 Z"/>
    </clipPath>
  </defs>

  <!-- Pocket flap (inside) -->
  <path class="pocket-flap" d="M162 847 L652 847 L650 858 L628 966 Q622 980 608 981 L285 981 L260 955 L250 955 Q230 972 205 970 Q182 966 180 930 Q178 905 194 895 L195 888 L164 859 Z"/>
  <line class="guide" x1="162" y1="858" x2="652" y2="858"/>
  <path class="slit" d="M479 869 A12 12 0 0 0 503 869"/>
  <path class="slit" d="M605 908 A12 12 0 0 0 605 932"/>

  <!-- Left side flap -->
  <g clip-path="url(#flapClip)">
    <rect class="panel-light" x="29" y="158" width="122" height="350"/>
    <rect class="band-red" x="29" y="508" width="122" height="45"/>
    <rect class="panel-dark" x="29" y="553" width="122" height="294"/>
  </g>
  <path class="cut-line" d="M151 158 L60 178 Q29 188 29 206"/>
  <path class="slit" d="M57 745 L57 755 L113 811 L124 811"/>

  <!-- Back panel + spine -->
  <rect class="panel-light" x="151" y="158" width="526" height="350"/>
  <rect class="band-red" x="151" y="508" width="526" height="45"/>
  <rect class="panel-dark" x="151" y="553" width="526" height="294"/>

  <!-- Front panel -->
  <rect role="img" aria-label="Foto: Glasfassade eines Hochhauses von unten gegen hellen Himmel" x="677" y="158" width="480" height="350" fill="url(#towerPhoto)"/>
  <rect class="band-red" x="653" y="508" width="504" height="45"/>
  <rect class="panel-light" x="677" y="553" width="480" height="294"/>
  <line class="cut-line" x1="677" y1="158" x2="1157" y2="158"/>
  <line class="cut-line" x1="1157" y1="158" x2="1157" y2="847"/>

  <!-- Fold guides -->
  <line class="guide" x1="151" y1="158" x2="151" y2="847"/>
  <line class="guide" x1="162" y1="158" x2="162" y2="847"/>
  <line class="guide" x1="653" y1="158" x2="653" y2="847"/>
  <line class="guide" x1="666" y1="158" x2="666" y2="847"/>

  <!-- Side flap content -->
  <g class="flap-brand">
    <rect class="brand-mark" x="70" y="270" width="30" height="30"/>
    <text class="brand-name" x="150" y="361" text-anchor="end" font-size="11.5">Wohnwert</text>
    <text class="brand-name" x="150" y="373" text-anchor="end" font-size="9">Elbland AG</text>
    <text class="brand-url" x="150" y="384" text-anchor="end" font-size="6.5">www.wwe-ag.de</text>
  </g>
  <g class="contact contact-dark" text-anchor="middle">
    <text x="115" y="425">Lindenhain-Straße 12</text>
    <text x="115" y="437">01468 Moritzdorf</text>
    <text x="115" y="448">03 51 / 40 00 12 34</text>
    <text x="115" y="460">03 51 / 40 00 12 35</text>
    <text x="115" y="471">info@wwe-ag.de</text>
    <text x="115" y="483">www.wwe-ag.de</text>
  </g>
  <g class="slogan" font-size="15" transform="translate(100 672) rotate(90)" text-anchor="middle">
    <text x="0" y="-6">Ihre Zufriedenheit,</text>
    <text x="0" y="13">ist unsere Motivation!</text>
  </g>

  <!-- Back panel content -->
  <g class="back-brand">
    <rect class="brand-mark" x="377" y="240" width="52" height="52"/>
    <text class="brand-name" x="511" y="414" text-anchor="end" font-size="19">Wohnwert</text>
    <text class="brand-name" x="511" y="434" text-anchor="end" font-size="15">Elbland AG</text>
    <text class="brand-url" x="511" y="452" text-anchor="end" font-size="11">www.wwe-ag.de</text>
  </g>
  <text class="band-url" x="438" y="538" text-anchor="middle">www.wwe-ag.de</text>
  <g class="contact contact-light" text-anchor="middle">
    <text x="443" y="748">Lindenhain-Straße 12</text>
    <text x="443" y="759.5">01468 Moritzdorf</text>
    <text x="443" y="771">03 51 / 40 00 12 34</text>
    <text x="443" y="782.5">03 51 / 40 00 12 35</text>
    <text x="443" y="794">info@wwe-ag.de</text>
    <text x="443" y="805.5">www.wwe-ag.de</text>
  </g>

  <!-- Front panel content -->
  <text class="slogan" x="917" y="535" text-anchor="middle" font-size="18.5">Ihre Zufriedenheit, ist unsere Motivation!</text>
  <g class="front-brand">
    <rect class="brand-mark" x="985" y="597" width="52" height="52"/>
    <text class="brand-name" x="1119" y="772" text-anchor="end" font-size="19">Wohnwert</text>
    <text class="brand-name" x="1119" y="792" text-anchor="end" font-size="15">Elbland AG</text>
    <text class="brand-url" x="1119" y="810" text-anchor="end" font-size="11">www.wwe-ag.de</text>
  </g>
</svg>
</body>
</html>
```